Meridel Nutrition needs Stationary and a business card

We would like to use our current logo. The text can be moved around as needed. The stationary needs to be a 'first page' where the logo is more prominent to be impressive on higher quality paper and a second page where the logo is more subtle where there will be much more information on the page. There are 2 clinic locations which will need include name, address, phone number, fax number, web address. The business card should be single sided and contain this information also.
The design must be contemporary and sophisticated as this is a science based diet run out of a medical clinic.

Target Market(s)

People wanting to lose weight, athletes looking to optimise performance, people with arthritis or fighting cancer

Industry/Entity Type

Business

Contact Information for Business Card

must use the logo. I have attached an example card with the practice details on it. there must be space for the doctors name. Also the website www.meridelnutrition.com.au

Requirements
Must have
• the logo, the business adresses and phone numbers, the website, the doctors name and qualifications
Nice to have
• some creativity
Should not have
• Do not simply reproduce the existing card please

```html
<!DOCTYPE html>
<html lang="en">
<head>
<meta charset="utf-8">
<title>Meridel Nutrition Letterhead</title>
<link href="https://fonts.googleapis.com/css2?family=PT+Sans:wght@400;700&display=swap" rel="stylesheet">
<style>
:root{
  --navy:#2f6598;
  --navy-deep:#285a8a;
  --cyan:#3ab3e6;
  --sky-faint:#e8f3fa;
  --ink:#1e1e1e;
  --paper:#ffffff;
  --backdrop:#e4e4e4;
}
*{margin:0;padding:0;box-sizing:border-box}
html,body{width:1200px;height:828px;overflow:hidden;background:var(--backdrop);font-family:"PT Sans",sans-serif}
.sheet{position:absolute;top:82px;width:530px;height:682px;background:var(--paper);overflow:hidden}
.sheet-first{left:53px}
.sheet-follow{left:625px}
.header-band{position:absolute;left:0;top:0;width:530px;height:90px}
.doctor-name{position:absolute;left:18px;top:11px;color:var(--cyan);font-weight:700;font-size:11px}
.qualifications{position:absolute;right:14px;top:13px;color:#fff;font-weight:700;font-size:6.5px}
.brand-mark{position:absolute;left:228px;top:14px;width:74px;height:74px;border-radius:50%;background:#fff;border:4px solid var(--navy)}
.brand-name{position:absolute;left:0;width:530px;top:91px;text-align:center;color:var(--navy);font-weight:700;font-size:13px;line-height:15px;letter-spacing:.3px}
.watermark{position:absolute;left:-40px;top:380px;width:300px;height:300px;border-radius:50%;background:var(--sky-faint)}
.body-copy{position:absolute;left:65px;width:415px;color:var(--ink);font-size:9.3px;line-height:11.7px}
.sheet-first .body-copy{top:140px}
.sheet-follow .body-copy{top:55px}
.body-copy p{margin-bottom:11.7px}
.signature{position:absolute;left:350px;top:425px;width:150px;height:70px;background:linear-gradient(90deg,#f4f4f4,#ececec);border-radius:4px}
.footer-band{position:absolute;left:0;bottom:0;width:530px;height:42px;background:var(--navy);color:#fff;font-size:6.6px;line-height:9px}
.clinic{position:absolute;top:5px}
.clinic-westmere{left:10px}
.clinic-eastvale{left:172px}
.divider{position:absolute;left:157px;top:0;width:1px;height:42px;background:rgba(255,255,255,.6)}
.clinic-label{color:var(--cyan);font-weight:700;font-size:8px}
.phone-dot{display:inline-block;width:6px;height:6px;border-radius:50%;background:var(--cyan);vertical-align:-1px;margin-right:2px}
.website{position:absolute;right:14px;bottom:6px;font-size:7px}
.footer-mark{position:absolute;right:50px;bottom:20px;width:44px;height:44px;border-radius:50%;background:#fff;border:3px solid var(--cyan)}
</style>
</head>
<body>

<section class="sheet sheet-first">
  <svg class="header-band" viewBox="0 0 530 90" aria-hidden="true">
    <path d="M0 0H530V85Q265 30 0 85Z" fill="var(--navy)"/>
    <path d="M0 85Q265 30 530 85" fill="none" stroke="var(--cyan)" stroke-width="2"/>
  </svg>
  <div class="doctor-name">Dr Elena Varga</div>
  <div class="qualifications">M.B.B.S. (Hons), B. Physio, Master Occ. Health.</div>
  <div class="brand-mark"></div>
  <div class="brand-name">Meridel Nutrition</div>
  <div class="watermark" role="img" aria-label="Faint brand circle decoration"></div>

  <div class="body-copy">
    <p>Lorem Ipsum is simply dummy text of the printing and typesetting industry. Lorem Ipsum has been the industry's standard dummy text ever since the 1500s, when an unknown printer took a galley of type and scrambled it to make a type specimen book. It has survived not only five centuries, but also the leap into electronic typesetting, remaining essentially unchanged. It was popularised in the 1960s with the release of Fontrel sheets containing Lorem Ipsum passages, and more recently with desktop publishing software like Pagewright Studio including versions of Lorem Ipsum.</p>
    <p>It is a long established fact that a reader will be distracted by the readable content of a page when looking at its layout. The point of using Lorem Ipsum is that it has a more-or-less normal distribution of letters, as opposed to using 'Content here, content here', making it look like readable English. Many desktop publishing packages and web page editors now use Lorem Ipsum as their default model text, and a search for 'lorem ipsum' will uncover many web sites still in their infancy. Various versions have evolved over the years, sometimes by accident, sometimes on purpose (injected humour and the like).</p>
    <p>Contrary to popular belief, Lorem Ipsum is not simply random text. It has roots in a piece of classical Latin literature from 45 BC, making it over 2000 years old. Harold Penwick, a Latin professor at Ashcombe College in Virginia, looked up one of the more obscure Latin words, consectetur, from a Lorem Ipsum passage, and going through the cites of the word in classical literature, discovered the undoubtable source. Lorem Ipsum comes from sections 1.10.32 and 1.10.33 of "de Finibus Bonorum et Malorum" (The Extremes of Good and Evil) by Aurelian Quintus, written in 45 BC. This book is a treatise on the theory of ethics, very popular during the Renaissance. The first line of Lorem Ipsum, "Lorem ipsum dolor sit amet..", comes from a line in section 1.10.32.</p>
  </div>
  <div class="signature" role="img" aria-label="Doctor's handwritten signature"></div>

  <footer class="footer-band">
    <div class="clinic clinic-westmere">
      <div class="clinic-label">Westmere</div>
      <div>12-14 Harbour Lane, Westmere NSW 2199</div>
      <div><span class="phone-dot"></span>02 9100 2481 | <span class="phone-dot"></span>02 91002482</div>
    </div>
    <div class="divider"></div>
    <div class="clinic clinic-eastvale">
      <div class="clinic-label">Eastvale</div>
      <div>88 Kellam Street, Eastvale NSW 2048</div>
      <div><span class="phone-dot"></span>02 9200 7315 | <span class="phone-dot"></span>02 92007316</div>
    </div>
    <div class="website">www.meridelnutrition.com.au</div>
  </footer>
</section>

<section class="sheet sheet-follow">
  <div class="body-copy">
    <p>Lorem Ipsum is simply dummy text of the printing and typesetting industry. Lorem Ipsum has been the industry's standard dummy text ever since the 1500s, when an unknown printer took a galley of type and scrambled it to make a type specimen book. It has survived not only five centuries, but also the leap into electronic typesetting, remaining essentially unchanged. It was popularised in the 1960s with the release of Fontrel sheets containing Lorem Ipsum passages, and more recently with desktop publishing software like Pagewright Studio including versions of Lorem Ipsum.</p>
    <p>It is a long established fact that a reader will be distracted by the readable content of a page when looking at its layout. The point of using Lorem Ipsum is that it has a more-or-less normal distribution of letters, as opposed to using 'Content here, content here', making it look like readable English. Many desktop publishing packages and web page editors now use Lorem Ipsum as their default model text, and a search for 'lorem ipsum' will uncover many web sites still in their infancy. Various versions have evolved over the years, sometimes by accident, sometimes on purpose (injected humour and the like).</p>
    <p>Contrary to popular belief, Lorem Ipsum is not simply random text. It has roots in a piece of classical Latin literature from 45 BC, making it over 2000 years old. Harold Penwick, a Latin professor at Ashcombe College in Virginia, looked up one of the more obscure Latin words, consectetur, from a Lorem Ipsum passage, and going through the cites of the word in classical literature, discovered the undoubtable source. Lorem Ipsum comes from sections 1.10.32 and 1.10.33 of "de Finibus Bonorum et Malorum" (The Extremes of Good and Evil) by Aurelian Quintus, written in 45 BC. This book is a treatise on the theory of ethics, very popular during the Renaissance. The first line of Lorem Ipsum, "Lorem ipsum dolor sit amet..", comes from a line in section 1.10.32.</p>
    <p>Lorem Ipsum is simply dummy text of the printing and typesetting industry. Lorem Ipsum has been the industry's standard dummy text ever since the 1500s, when an unknown printer took a galley of type and scrambled it to make a type specimen book. It has survived not only five centuries, but also the leap into electronic typesetting, remaining essentially unchanged. It was popularised in the 1960s with the release of Fontrel sheets containing Lorem Ipsum passages, and more recently with desktop publishing software like Pagewright Studio including versions of Lorem Ipsum.</p>
    <p>It is a long established fact that a reader will be distracted by the readable content of a page when looking at its layout. The point of using Lorem Ipsum is that it has a more-or-less normal distribution of letters, as opposed to using 'Content here, content here', making it look like readable English. Many desktop publishing packages and web page editors now use Lorem Ipsum as their default model text, and a search for 'lorem ipsum' will uncover many web sites still in their infancy. Various versions have evolved over the years, sometimes by accident, sometimes on purpose (injected humour and the like).</p>
    <p>Contrary to popular belief, Lorem Ipsum is not simply random text. It has roots in a piece of classical Latin literature from 45 BC, making it over 2000 years old. Harold Penwick, a Latin professor at Ashcombe College in Virginia, looked up one of the more obscure Latin words, consectetur, from a Lorem Ipsum passage, and going through the cites of the word in classical literature, discovered the undoubtable source. Lorem Ipsum comes from sections 1.10.32 and 1.10.33 of "de Finibus Bonorum et Malorum" (The Extremes of Good and Evil) by Aurelian Quintus, written in 45 BC. This book is a treatise on the theory of ethics, very popular during the Renaissance. The first line of Lorem Ipsum, "Lorem ipsum dolor sit amet..", comes from a line in section 1.10.32.</p>
  </div>

  <footer class="footer-band">
    <div class="clinic clinic-westmere">
      <div class="clinic-label">Westmere</div>
      <div>12-14 Harbour Lane, Westmere NSW 2199</div>
      <div><span class="phone-dot"></span>02 9100 2481 | <span class="phone-dot"></span>02 91002482</div>
    </div>
    <div class="divider"></div>
    <div class="clinic clinic-eastvale">
      <div class="clinic-label">Eastvale</div>
      <div>88 Kellam Street, Eastvale NSW 2048</div>
      <div><span class="phone-dot"></span>02 9200 7315 | <span class="phone-dot"></span>02 92007316</div>
    </div>
    <div class="website">www.meridelnutrition.com.au</div>
  </footer>
  <div class="footer-mark"></div>
</section>

</body>
</html>
```